Love pets? Create a veterinary business card that aligns with our new revamped website.

Greetings! We are a five-doctor veterinary hospital that seeks your expertise in designing a new business card that harmonizes with our recently revitalized website: www.lmcr.net. The card should feature our logo, the five doctors, operating hours, contact information, and communicate our purpose and personality.

Contact Information for Business Card

TBA

```html
<!DOCTYPE html>
<html lang="en">
<head>
<meta charset="utf-8">
<title>Lakemont Creek Veterinary Hospital – Business Card</title>
<link href="https://fonts.googleapis.com/css2?family=Arimo:wght@400;700&display=swap" rel="stylesheet">
<style>
  :root {
    --backdrop: #e8e8e6;
    --card-white: #ffffff;
    --brand-green: #3f8a35;
    --brand-green-deep: #3a7f33;
    --brand-green-light: #5aa84c;
    --text-grey: #6b6b6b;
    --rule-grey: #9a9a9a;
  }
  * { box-sizing: border-box; margin: 0; padding: 0; }
  html, body { width: 1200px; height: 802px; overflow: hidden; }
  body {
    background: var(--backdrop);
    font-family: "Arimo", Arial, sans-serif;
    position: relative;
  }
  .card {
    position: absolute;
    top: 246px;
    width: 540px;
    height: 309px;
    box-shadow: 0 6px 18px rgba(0,0,0,0.12);
  }
  /* Front side */
  .card-front { left: 45px; background: var(--card-white); }
  .card-front .corner-tab {
    position: absolute; top: 0; right: 24px;
    width: 30px; height: 6px; background: var(--brand-green);
  }
  .card-front .doctor-name {
    position: absolute; top: 34px; right: 28px;
    font-size: 18px; font-weight: 700; color: var(--brand-green);
  }
  .wordmark {
    position: absolute; display: flex; align-items: center; gap: 10px;
    font-weight: 700; color: var(--brand-green);
  }
  .wordmark .mark-dot {
    width: 30px; height: 30px; border-radius: 50%; background: currentColor; flex: none;
  }
  .wordmark .name { line-height: 1.1; }
  .card-front .wordmark { left: 30px; top: 86px; font-size: 22px; }
  .contact-list {
    position: absolute; left: 72px; top: 150px; list-style: none;
    font-size: 14px; color: var(--text-grey);
  }
  .contact-list li { display: flex; align-items: center; gap: 8px; height: 21px; }
  .contact-list svg { width: 12px; height: 12px; flex: none; }
  .card-front .divider {
    position: absolute; left: 72px; right: 28px; top: 245px;
    height: 1px; background: var(--rule-grey);
  }
  .card-front .address {
    position: absolute; left: 72px; top: 256px;
    font-size: 14px; color: var(--text-grey);
  }
  /* Back side */
  .card-back {
    left: 615px;
    background: radial-gradient(ellipse at 30% 60%, var(--brand-green-light) 0%, var(--brand-green) 45%, var(--brand-green-deep) 100%);
  }
  .card-back .wordmark {
    left: 150px; top: 128px; font-size: 26px; color: #ffffff;
  }
</style>
</head>
<body>
  <section class="card card-front" aria-label="Business card front">
    <div class="corner-tab"></div>
    <p class="doctor-name">Dana Whitford, DVM</p>
    <div class="wordmark">
      <span class="mark-dot"></span>
      <span class="name">Lakemont Creek<br>Veterinary Hospital</span>
    </div>
    <ul class="contact-list">
      <li>
        <svg viewBox="0 0 12 12" aria-hidden="true"><path d="M2.5 1.5l2 2-1 1.2c.7 1.4 1.8 2.5 3.2 3.2l1.2-1 2 2-1.3 1.6C5.2 10.2 1.8 6.8 1.5 3z" fill="none" stroke="#3f8a35" stroke-width="1.1"/></svg>
        (555) 214-3090
      </li>
      <li>
        <svg viewBox="0 0 12 12" aria-hidden="true"><rect x="3" y="1" width="6" height="3.5" fill="none" stroke="#3f8a35"/><rect x="1" y="4.5" width="10" height="4.5" fill="none" stroke="#3f8a35"/><rect x="3" y="7.5" width="6" height="3.5" fill="#fff" stroke="#3f8a35"/></svg>
        (555) 214-3091
      </li>
      <li>
        <svg viewBox="0 0 12 12" aria-hidden="true"><rect x="1" y="2.5" width="10" height="7" fill="none" stroke="#3f8a35"/><path d="M1 2.5l5 4 5-4" fill="none" stroke="#3f8a35"/></svg>
        info@lmcr.net
      </li>
      <li>
        <svg viewBox="0 0 12 12" aria-hidden="true"><circle cx="6" cy="6" r="5" fill="#3f8a35"/><path d="M1 6h10M6 1c-2.5 3-2.5 7 0 10M6 1c2.5 3 2.5 7 0 10" fill="none" stroke="#fff" stroke-width="0.7"/></svg>
        www.lmcr.net
      </li>
    </ul>
    <div class="divider"></div>
    <p class="address">4820 Meadow Crest Road, Springdale, TX 75001</p>
  </section>

  <section class="card card-back" aria-label="Business card back">
    <div class="wordmark">
      <span class="mark-dot"></span>
      <span class="name">Lakemont Creek<br>Veterinary Hospital</span>
    </div>
  </section>
</body>
</html>
```